Postcard Design

The Willow Bend Courier ~ Your #1 Newspaper since 1971

I am trying to reach new clients with our special of
Receive 1 month free with a year contract.

The Willow Bend Courier is a monthly newspaper that readers cherish like a magazine waiting for the next one to be published. I have had several advertisers since the first paper in 1971. My mom was the prior owner and she loved roosters, hence the rooster in the logo.
Updates

Please add the following:

Your # 1 Newspaper 

Serving Ocean County since 1971

1 Month FREE with 1 Year Contract

Instead of your #1 Newspaper...please put

The areas best place to see what's happening locally.

Target Market(s)

professionals, restaurants, etc.

Colors
33b7a4
85cae6
33a6d7

Requirements
Must have
• P.O. Box 457, Willow Bend, NJ 08314
Email: info@willowbendcourier.example
609.555.0182
www.willowbendcourier.example
Nice to have
• Typical savings up to $300.

```html
<!DOCTYPE html>
<html lang="en">
<head>
<meta charset="utf-8">
<title>The Willow Bend Courier – Postcard</title>
<link rel="stylesheet" href="https://fonts.googleapis.com/css2?family=Roboto:wght@400;700&family=Oswald:wght@500&display=swap">
<style>
  :root {
    --teal: #33b7a4;
    --sky: #85cae6;
    --blue: #33a6d7;
    --navy: #1f3a4d;
    --ink: #3b3b3b;
    --gold: #f6d95a;
    --red: #e0493f;
    --paper: #ffffff;
  }
  html, body { margin: 0; padding: 0; overflow: hidden; background: var(--paper); }
  .postcard {
    position: relative;
    width: 1200px;
    height: 929px;
    overflow: hidden;
    background: var(--paper);
    font-family: "Roboto", Arial, sans-serif;
    color: var(--ink);
  }
  .ribbon {
    position: absolute;
    display: flex;
    align-items: center;
    justify-content: center;
    box-sizing: border-box;
  }
  .ribbon svg { position: absolute; inset: 0; width: 100%; height: 100%; }
  .ribbon span { position: relative; white-space: nowrap; }

  .offer-ribbon { left: 281px; top: 48px; width: 919px; height: 100px; padding-left: 60px; }
  .offer-ribbon span { color: var(--paper); font-size: 38px; letter-spacing: 0.5px; }
  .offer-ribbon strong { color: var(--gold); font-weight: 700; }

  .title-band { left: 498px; top: 163px; width: 657px; height: 74px; padding-left: 40px; }
  .title-band span {
    font-family: "Oswald", "Arial Narrow", sans-serif;
    font-weight: 500;
    font-size: 33px;
    color: var(--navy);
    letter-spacing: 1px;
  }

  .mascot-art {
    position: absolute;
    left: 40px; top: 190px;
    width: 460px; height: 550px;
    border-radius: 48% 52% 40% 45% / 45% 50% 40% 48%;
    background: radial-gradient(circle at 45% 40%, #f2b84a 0%, #e86a8f 35%, #7fc6d9 65%, rgba(255,255,255,0) 78%);
    opacity: 0.85;
  }

  .highlights {
    position: absolute;
    left: 636px; top: 336px;
    width: 500px;
    margin: 0; padding: 0;
    list-style: none;
    font-size: 28px;
    line-height: 1.1;
  }
  .highlights li {
    position: relative;
    padding-left: 42px;
    margin-bottom: 52px;
  }
  .highlights li::before {
    content: "";
    position: absolute;
    left: 0; top: 6px;
    width: 18px; height: 18px;
    border-radius: 50%;
    background: var(--paper);
    border: 4px solid var(--red);
    box-sizing: border-box;
  }

  .web-ribbon { left: 563px; top: 755px; width: 637px; height: 89px; padding-left: 30px; }
  .web-ribbon span { color: var(--gold); font-size: 34px; }

  .brand-name {
    position: absolute;
    left: 40px; top: 775px;
    width: 460px;
    text-align: center;
    font-weight: 700;
    font-size: 38px;
    color: var(--navy);
  }

  .contact-line {
    position: absolute;
    left: 0; top: 872px;
    width: 1200px;
    text-align: center;
    font-size: 22px;
    color: var(--ink);
  }
  .contact-line .sep { color: var(--teal); margin: 0 14px; }
</style>
</head>
<body>
<main class="postcard">
  <div class="mascot-art" role="img" aria-label="Colourful ornamental rooster illustration"></div>

  <div class="ribbon offer-ribbon">
    <svg viewBox="0 0 919 100" preserveAspectRatio="none" aria-hidden="true">
      <polygon points="0,0 919,0 919,100 0,100 36,50" fill="var(--teal)"/>
    </svg>
    <span>1 Month <strong>FREE</strong> with 1 Year Contract</span>
  </div>

  <div class="ribbon title-band">
    <svg viewBox="0 0 657 74" preserveAspectRatio="none" aria-hidden="true">
      <polygon points="0,0 657,0 657,74 0,74 28,37" fill="var(--sky)"/>
    </svg>
    <span>THE WILLOW BEND COURIER</span>
  </div>

  <ul class="highlights">
    <li>Serving Ocean County since 1971</li>
    <li>The areas best place to see what's happening locally</li>
    <li>Typical savings up to $300</li>
  </ul>

  <div class="ribbon web-ribbon">
    <svg viewBox="0 0 637 89" preserveAspectRatio="none" aria-hidden="true">
      <polygon points="0,0 637,0 637,89 0,89 32,44.5" fill="var(--teal)"/>
    </svg>
    <span>www.willowbendcourier.example</span>
  </div>

  <div class="brand-name">The Willow Bend Courier</div>

  <p class="contact-line">
    P.O. Box 457, Willow Bend, NJ 08314<span class="sep">|</span>Email: info@willowbendcourier.example<span class="sep">|</span>609.555.0182
  </p>
</main>
</body>
</html>
```